2 Ridgeway Bills Motor Care Banners

Looking to have two pull up banners designed - each 33.5 x 80

First banner- Scheduled Maintenance, Diagnostics, Inspections
Voted Finest of Carrow 3 years in a row!

Second banner- Brakes, Tires, General Auto Service
Include the 3 FOC logos
2019, 2018, 2017

```html
<!DOCTYPE html>
<html lang="en">
<head>
<meta charset="utf-8">
<title>Ridgeway Bills Motor Care – Pull Up Banners</title>
<link rel="stylesheet" href="https://fonts.googleapis.com/css2?family=Oswald:wght@600&family=Montserrat:wght@500&family=Roboto+Condensed:wght@400;700&display=swap">
<style>
  :root{
    --navy:#3e4461;
    --plate:#4d5470;
    --plate-dark:#434a66;
    --gold:#c5b55e;
    --red:#d4213d;
    --white:#ffffff;
    --page:#ffffff;
    --photo-light:#9a9ea8;
    --photo-dark:#7d818c;
  }
  *{box-sizing:border-box;margin:0;padding:0}
  html,body{width:1067px;height:1200px;overflow:hidden;background:var(--page)}
  .canvas{position:relative;width:1067px;height:1200px}
  .banner{position:absolute;top:14px;width:489px;height:1169px;background:var(--navy);overflow:hidden}
  .banner--left{left:20px}
  .banner--right{left:559px}
  .band-top{position:absolute;left:0;top:0;width:100%;height:16px;background:var(--gold)}
  .band-bottom{position:absolute;left:0;bottom:0;width:100%;height:39px;background:var(--gold)}
  .header{position:absolute;left:0;top:16px;width:100%;height:148px;background:linear-gradient(180deg,var(--plate),var(--plate-dark));text-align:center}
  .brand-name{font-family:"Oswald",sans-serif;font-weight:600;color:var(--gold);font-size:54px;line-height:1;padding-top:20px;letter-spacing:1.5px}
  .brand-sub{font-family:"Montserrat",sans-serif;font-weight:500;color:var(--white);font-size:19px;letter-spacing:5px;margin-top:30px}
  .hero{position:absolute;left:0;top:164px}
  .award-seal{position:absolute;left:278px;top:405px;width:172px;height:172px;border-radius:50%;background:var(--red);border:7px solid var(--white);box-shadow:0 2px 6px rgba(0,0,0,.35);color:var(--white);text-align:center;font-family:"Roboto Condensed",sans-serif;font-weight:700;line-height:1.02;padding-top:26px}
  .award-seal .top{font-size:26px}
  .award-seal .big{font-size:36px;line-height:1.05}
  .award-seal .small{font-size:20px}
  .services{position:absolute;left:0;top:650px;width:100%;list-style:none}
  .service{position:absolute;left:88px;display:flex;align-items:center}
  .service-icon{width:88px;height:88px;border-radius:50%;border:2px solid var(--white);display:flex;align-items:center;justify-content:center;flex:none}
  .service-label{margin-left:46px;font-family:"Oswald",sans-serif;font-weight:600;font-size:30px;line-height:1.25;color:var(--gold);letter-spacing:.8px}
  .footer-rule{position:absolute;left:89px;width:311px;height:4px}
  .footer-rule--gold{top:1030px;background:var(--gold)}
  .footer-rule--white{top:1127px;height:3px;background:var(--white)}
  .footer{position:absolute;left:10px;top:1034px;width:469px;height:96px;background:linear-gradient(180deg,var(--plate),var(--plate-dark))}
  .contact{position:absolute;left:92px;display:flex;align-items:center;font-family:"Roboto Condensed",sans-serif;color:var(--white);font-size:32px;letter-spacing:.5px}
  .contact svg{margin-right:14px}
  .contact--web{top:4px}
  .contact--phone{top:48px}
  .award-row{position:absolute;left:0;top:14px;width:100%;display:flex;justify-content:space-around;padding:0 6px}
  .award-badge{display:flex;align-items:center;gap:6px}
  .award-badge .disc{width:56px;height:56px;border-radius:50%;background:#e7e9ee;border:3px solid #c9ccd6}
  .award-badge .tag{width:66px;height:56px;background:var(--white);border-top:22px solid var(--red)}
</style>
</head>
<body>
<div class="canvas">

  <section class="banner banner--left">
    <div class="band-top"></div>
    <header class="header">
      <div class="brand-name">Ridgeway Bills</div>
      <div class="brand-sub">MOTOR CARE</div>
    </header>

    <svg class="hero" width="489" height="620" viewBox="0 0 489 620">
      <defs>
        <linearGradient id="photoToneLeft" x1="0" y1="0" x2="0" y2="1">
          <stop offset="0" stop-color="var(--photo-light)"/>
          <stop offset="1" stop-color="var(--photo-dark)"/>
        </linearGradient>
      </defs>
      <path role="img" aria-label="Photo of the shop front with its gabled entrance" fill="url(#photoToneLeft)" d="M0 0H489V570C455 480 380 420 250 408C130 398 40 385 0 300Z"/>
      <path fill="var(--gold)" d="M0 300C40 385 130 398 250 408C380 420 455 480 489 570V612C450 510 380 452 250 436C120 422 30 410 0 338Z"/>
    </svg>

    <div class="award-seal">
      <div class="top">Finest of</div>
      <div class="big">Carrow</div>
      <div class="small">3 years<br>in a row!</div>
    </div>

    <ul class="services">
      <li class="service" style="top:0">
        <span class="service-icon">
          <svg width="50" height="50" viewBox="0 0 50 50" fill="none" stroke="var(--gold)" stroke-width="3" stroke-linecap="round">
            <circle cx="22" cy="24" r="10"/><circle cx="22" cy="24" r="4"/>
            <path d="M22 8v4M22 36v4M6 24h4M34 24h4M11 13l3 3M30 32l3 3M11 35l3-3M30 16l3-3"/>
            <circle cx="37" cy="37" r="7" fill="var(--navy)"/><path d="M37 33v4h3"/>
          </svg>
        </span>
        <span class="service-label">Scheduled<br>Maintenance</span>
      </li>
      <li class="service" style="top:117px">
        <span class="service-icon">
          <svg width="56" height="44" viewBox="0 0 56 44" fill="none" stroke="var(--gold)" stroke-width="3" stroke-linejoin="round">
            <rect x="20" y="4" width="30" height="24" fill="var(--navy)"/>
            <path d="M24 22l8-8 6 5 8-10"/><path d="M14 34h40"/>
            <path d="M4 32l4-12h12v16H4z" fill="var(--gold)"/>
          </svg>
        </span>
        <span class="service-label">Diagnostics</span>
      </li>
      <li class="service" style="top:236px">
        <span class="service-icon">
          <svg width="44" height="50" viewBox="0 0 44 50" fill="none" stroke="var(--gold)" stroke-width="3" stroke-linejoin="round">
            <rect x="5" y="6" width="30" height="40"/><rect x="13" y="2" width="14" height="7" fill="var(--navy)"/>
            <path d="M10 18h20M10 24h14"/>
            <circle cx="32" cy="38" r="9" fill="var(--gold)" stroke="none"/>
            <path d="M27 38l4 4 6-7" stroke="var(--navy)"/>
          </svg>
        </span>
        <span class="service-label">Inspections</span>
      </li>
    </ul>

    <div class="footer-rule footer-rule--gold"></div>
    <div class="footer">
      <div class="contact contact--web">
        <svg width="30" height="30" viewBox="0 0 30 30" fill="none" stroke="var(--white)" stroke-width="2">
          <circle cx="19" cy="11" r="9"/><path d="M10 11h18M19 2c-4 5-4 13 0 18M19 2c4 5 4 13 0 18"/><path d="M12 18l-9 9" stroke-width="3"/>
        </svg>
        www.rbmotorcare.app
      </div>
      <div class="contact contact--phone">
        <svg width="26" height="26" viewBox="0 0 24 24" fill="var(--white)">
          <path d="M6.6 10.8a15 15 0 0 0 6.6 6.6l2.2-2.2c.3-.3.7-.4 1-.2 1.1.4 2.3.6 3.6.6.6 0 1 .4 1 1V20c0 .6-.4 1-1 1A17 17 0 0 1 3 4c0-.6.4-1 1-1h3.5c.6 0 1 .4 1 1 0 1.3.2 2.5.6 3.6.1.3 0 .7-.2 1z"/>
        </svg>
        555-014-2290
      </div>
    </div>
    <div class="footer-rule footer-rule--white"></div>
    <div class="band-bottom"></div>
  </section>

  <section class="banner banner--right">
    <div class="band-top"></div>
    <header class="header">
      <div class="brand-name">Ridgeway Bills</div>
      <div class="brand-sub">MOTOR CARE</div>
    </header>

    <svg class="hero" width="489" height="620" viewBox="0 0 489 620">
      <defs>
        <linearGradient id="photoToneRight" x1="0" y1="0" x2="0" y2="1">
          <stop offset="0" stop-color="var(--photo-light)"/>
          <stop offset="1" stop-color="var(--photo-dark)"/>
        </linearGradient>
      </defs>
      <g transform="translate(489 0) scale(-1 1)">
        <path role="img" aria-label="Photo of the service bays with cars parked in front of the shop" fill="url(#photoToneRight)" d="M0 0H489V570C455 480 380 420 250 408C130 398 40 385 0 300Z"/>
        <path fill="var(--gold)" d="M0 300C40 385 130 398 250 408C380 420 455 480 489 570V612C450 510 380 452 250 436C120 422 30 410 0 338Z"/>
      </g>
    </svg>

    <ul class="services">
      <li class="service" style="top:0">
        <span class="service-icon">
          <svg width="52" height="44" viewBox="0 0 52 44" fill="var(--gold)">
            <path d="M4 10l14-6 10 18-14 6z"/><path d="M22 28l22-8 4 10-24 10z"/><path d="M30 6h10v6H30z"/>
          </svg>
        </span>
        <span class="service-label">Brakes</span>
      </li>
      <li class="service" style="top:117px">
        <span class="service-icon">
          <svg width="50" height="50" viewBox="0 0 50 50" fill="none" stroke="var(--gold)" stroke-width="3">
            <circle cx="20" cy="25" r="15"/><circle cx="20" cy="25" r="6"/>
            <path d="M20 10v9M20 31v9M5 25h9M26 25h9"/>
            <path d="M38 8v34M44 8v34M38 14h6M38 22h6M38 30h6M38 38h6"/>
          </svg>
        </span>
        <span class="service-label">Tires</span>
      </li>
      <li class="service" style="top:236px">
        <span class="service-icon">
          <svg width="50" height="46" viewBox="0 0 50 46" fill="none" stroke="var(--gold)" stroke-width="3" stroke-linejoin="round">
            <path d="M6 38V28l6-10h26l6 10v10z" fill="var(--navy)"/>
            <circle cx="14" cy="38" r="4" fill="var(--gold)"/><circle cx="36" cy="38" r="4" fill="var(--gold)"/>
            <path d="M22 4l10 10M30 4l-4 6" stroke-width="4" stroke-linecap="round"/>
          </svg>
        </span>
        <span class="service-label">General Auto<br>Service</span>
      </li>
    </ul>

    <div class="footer-rule footer-rule--gold"></div>
    <div class="footer">
      <div class="award-row">
        <div class="award-badge" role="img" aria-label="2017 Finest of Carrow award"><span class="disc"></span><span class="tag"></span></div>
        <div class="award-badge" role="img" aria-label="2018 Finest of Carrow award"><span class="disc"></span><span class="tag"></span></div>
        <div class="award-badge" role="img" aria-label="2019 Finest of Carrow award"><span class="disc"></span><span class="tag"></span></div>
      </div>
    </div>
    <div class="band-bottom"></div>
  </section>

</div>
</body>
</html>
```